Copperwell Mini Storage - Ad for half Page

Need half page ad for a publication.
would also like to be able to use in the future
self storage facility - 3 locations, the third opening soon
do not like real busy projects...i have a logo but willing to tweak if needed

```html
<!DOCTYPE html>
<html lang="en">
<head>
<meta charset="utf-8">
<title>Copperwell Mini Storage – Half Page Ad</title>
<link href="https://fonts.googleapis.com/css2?family=Archivo+Black&family=Montserrat:wght@500;600;700&family=Open+Sans:wght@400;600&display=swap" rel="stylesheet">
<style>
  :root {
    --backdrop: #a8b59e;
    --brown: #5b2a12;
    --brown-dark: #4a200c;
    --tan: #b9733f;
    --panel-light: #f7f7f7;
    --panel-mid: #e2e2e2;
    --panel-edge: #c9c9c9;
    --ink: #2b2b2b;
    --white: #ffffff;
  }
  * { box-sizing: border-box; margin: 0; padding: 0; }
  html, body { width: 1200px; height: 883px; overflow: hidden; }
  body { background: var(--backdrop); position: relative; font-family: "Open Sans", Arial, sans-serif; }

  .ad {
    position: absolute; left: 124px; top: 124px;
    width: 950px; height: 634px;
    background: var(--white);
    overflow: hidden;
  }

  .hero-photo {
    position: absolute; left: 0; top: 0; width: 431px; height: 513px;
    background: linear-gradient(100deg, #e9ecea 0%, #d9dfd6 35%, #b9d77a 60%, #c9b9a0 85%, #b89a7a 100%);
  }
  .accent-tab {
    position: absolute; left: 275px; top: 0; width: 0; height: 0;
  }

  .info-panel {
    position: absolute; left: 431px; top: 0; width: 519px; height: 513px;
    background: radial-gradient(ellipse at 40% 35%, var(--panel-light) 0%, var(--panel-mid) 65%, var(--panel-edge) 100%);
  }
  .headline {
    position: absolute; left: 12px; top: 12px;
    font-family: "Archivo Black", Arial, sans-serif;
    font-size: 84px; line-height: 82px;
    color: var(--brown);
    text-shadow: 2px 3px 4px rgba(0,0,0,0.25);
    letter-spacing: 0.5px;
  }
  .intro {
    position: absolute; left: 14px; top: 250px; width: 490px;
    font-size: 14px; line-height: 20px; color: var(--ink);
  }
  .features {
    position: absolute; left: 17px; top: 333px; list-style: none;
  }
  .features li {
    display: flex; align-items: center; gap: 10px;
    font-size: 15.5px; line-height: 24.7px; color: var(--ink);
  }
  .features svg { width: 13px; height: 13px; flex: none; }

  .unit-badge {
    position: absolute; left: 276px; width: 217px;
    border: 2px solid var(--brown); border-radius: 50%;
    background: var(--white);
    display: flex; align-items: center; gap: 10px; padding-left: 30px;
    box-shadow: 0 2px 4px rgba(0,0,0,0.15);
  }
  .unit-badge.climate { top: 327px; height: 86px; }
  .unit-badge.standard { top: 420px; height: 84px; }
  .unit-badge svg { width: 48px; height: 36px; flex: none; }
  .unit-badge span {
    font-family: "Montserrat", Arial, sans-serif; font-weight: 700;
    font-size: 15.5px; line-height: 16px; color: var(--ink);
  }

  .brand-bar {
    position: absolute; left: 0; top: 513px; width: 431px; height: 87px;
    background: var(--white);
    display: flex; align-items: center; padding-left: 78px; gap: 12px;
  }
  .brand-mark { width: 46px; height: 46px; background: var(--tan); flex: none; }
  .brand-name {
    font-family: "Montserrat", Arial, sans-serif; font-weight: 700;
    font-size: 22px; line-height: 25px; color: var(--brown);
  }

  .locations {
    position: absolute; left: 431px; top: 513px; width: 519px; height: 87px;
    background: var(--brown); color: var(--white);
    font-family: "Montserrat", Arial, sans-serif;
  }
  .locations-title {
    position: absolute; left: 26px; top: 8px;
    font-weight: 700; font-size: 15px; letter-spacing: 0.3px;
    display: flex; align-items: center; gap: 10px;
  }
  .location { position: absolute; top: 35px; }
  .location .city { font-weight: 600; font-size: 15.5px; line-height: 19px; }
  .location .phone { font-weight: 500; font-size: 15px; line-height: 19px; display: flex; align-items: center; gap: 4px; }
  .location .soon { font-weight: 500; font-size: 15px; line-height: 19px; letter-spacing: 0.4px; }
  .location.one { left: 26px; }
  .location.two { left: 187px; }
  .location.three { left: 354px; }

  .footer-web {
    position: absolute; left: 0; top: 600px; width: 431px; height: 34px;
    background: var(--brown-dark); color: var(--white);
    display: flex; align-items: center; padding-left: 76px; gap: 10px;
    font-size: 14.5px;
  }
  .footer-mail {
    position: absolute; left: 431px; top: 600px; width: 519px; height: 34px;
    background: var(--white); color: var(--brown);
    display: flex; align-items: center; padding-left: 26px; gap: 10px;
    font-size: 14.5px;
  }
</style>
</head>
<body>
<div class="ad">
  <div class="hero-photo" role="img" aria-label="Photo of two people in a bright self-storage hallway, one holding a tablet and one carrying a cardboard box, with stacked moving boxes and green unit doors"></div>

  <div class="info-panel">
    <h1 class="headline">NEED A<br>STORAGE<br>UNIT?</h1>
    <p class="intro">We are a family-owned, premier self-storage facility located in Millbrook and Cedar Falls. We offer solutions to your Personal Storage, Business Storage and RV &amp; Boat Storage needs.</p>
    <ul class="features">
      <li><svg viewBox="0 0 13 13"><rect width="13" height="13" rx="1.5" fill="#5b2a12"/><path d="M3 6.8l2.4 2.4L10 4.3" stroke="#fff" stroke-width="1.8" fill="none"/></svg>Safe &amp; Secure Units</li>
      <li><svg viewBox="0 0 13 13"><rect width="13" height="13" rx="1.5" fill="#5b2a12"/><path d="M3 6.8l2.4 2.4L10 4.3" stroke="#fff" stroke-width="1.8" fill="none"/></svg>Friendly &amp; Professional Staff</li>
      <li><svg viewBox="0 0 13 13"><rect width="13" height="13" rx="1.5" fill="#5b2a12"/><path d="M3 6.8l2.4 2.4L10 4.3" stroke="#fff" stroke-width="1.8" fill="none"/></svg>Electronic Gate Access</li>
      <li><svg viewBox="0 0 13 13"><rect width="13" height="13" rx="1.5" fill="#5b2a12"/><path d="M3 6.8l2.4 2.4L10 4.3" stroke="#fff" stroke-width="1.8" fill="none"/></svg>Online Account Access</li>
      <li><svg viewBox="0 0 13 13"><rect width="13" height="13" rx="1.5" fill="#5b2a12"/><path d="M3 6.8l2.4 2.4L10 4.3" stroke="#fff" stroke-width="1.8" fill="none"/></svg>No Deposit Required</li>
      <li><svg viewBox="0 0 13 13"><rect width="13" height="13" rx="1.5" fill="#5b2a12"/><path d="M3 6.8l2.4 2.4L10 4.3" stroke="#fff" stroke-width="1.8" fill="none"/></svg>Month-to-month Rentals</li>
      <li><svg viewBox="0 0 13 13"><rect width="13" height="13" rx="1.5" fill="#5b2a12"/><path d="M3 6.8l2.4 2.4L10 4.3" stroke="#fff" stroke-width="1.8" fill="none"/></svg>Security Camera Monitoring</li>
    </ul>

    <div class="unit-badge climate">
      <svg viewBox="0 0 48 36"><path d="M2 12L24 2l22 10v3H2z" fill="#5b2a12"/><rect x="5" y="15" width="38" height="20" fill="#5b2a12"/><rect x="9" y="18" width="22" height="15" fill="#fff"/><path d="M9 21h22M9 24h22M9 27h22M9 30h22" stroke="#5b2a12" stroke-width="1.3"/><rect x="35" y="17" width="4" height="12" rx="2" fill="#fff"/><circle cx="37" cy="30" r="3" fill="#fff"/><rect x="36.2" y="21" width="1.6" height="9" fill="#b9733f"/></svg>
      <span>Climate<br>Controlled<br>Units</span>
    </div>
    <div class="unit-badge standard">
      <svg viewBox="0 0 48 36"><path d="M2 12L24 2l22 10v3H2z" fill="#5b2a12"/><rect x="5" y="15" width="38" height="20" fill="#5b2a12"/><rect x="10" y="18" width="28" height="15" fill="#fff"/><path d="M10 21h28M10 24h28M10 27h28M10 30h28" stroke="#5b2a12" stroke-width="1.3"/></svg>
      <span>Non-Climate<br>Units</span>
    </div>
  </div>

  <div class="brand-bar">
    <div class="brand-mark"></div>
    <div class="brand-name">Copperwell<br>Mini Storage</div>
  </div>

  <div class="locations">
    <div class="locations-title">
      <svg width="10" height="14" viewBox="0 0 10 14"><path d="M5 0a5 5 0 0 0-5 5c0 3.6 5 9 5 9s5-5.4 5-9a5 5 0 0 0-5-5zm0 7a2 2 0 1 1 0-4 2 2 0 0 1 0 4z" fill="#fff"/></svg>
      3 CONVENIENT LOCATIONS
    </div>
    <div class="location one">
      <div class="city">Millbrook</div>
      <div class="phone"><svg width="9" height="9" viewBox="0 0 10 10"><path d="M2 0l2 2.5-1 1.3a6 6 0 0 0 3.2 3.2l1.3-1L10 8l-1.5 2C4 10 0 6 0 1.5z" fill="#fff"/></svg>555-201-4470</div>
    </div>
    <div class="location two">
      <div class="city">Cedar Falls</div>
      <div class="phone"><svg width="9" height="9" viewBox="0 0 10 10"><path d="M2 0l2 2.5-1 1.3a6 6 0 0 0 3.2 3.2l1.3-1L10 8l-1.5 2C4 10 0 6 0 1.5z" fill="#fff"/></svg>555-318-2265</div>
    </div>
    <div class="location three">
      <div class="city">Ridgeview @ Hwy 9</div>
      <div class="soon">COMING SOON!</div>
    </div>
  </div>

  <div class="footer-web">
    <svg width="12" height="12" viewBox="0 0 12 12"><circle cx="6" cy="6" r="5.3" fill="none" stroke="#fff" stroke-width="1.2"/><ellipse cx="6" cy="6" rx="2.3" ry="5.3" fill="none" stroke="#fff" stroke-width="1"/><path d="M0.7 6h10.6" stroke="#fff" stroke-width="1"/></svg>
    www.CopperwellMiniStorage.com
  </div>
  <div class="footer-mail">
    <svg width="13" height="10" viewBox="0 0 13 10"><rect width="13" height="10" rx="1" fill="#5b2a12"/><path d="M0.5 0.8L6.5 5.5l6-4.7" stroke="#fff" stroke-width="1.2" fill="none"/></svg>
    sales@CopperwellMiniStorage.com
  </div>
</div>
</body>
</html>
```